College Advising Business Card Design

We need a business card design for a new company. We advise students and their families on finding the right colleges to apply to; the application process; creating resumes; writing essays; and once students are accepted, figuring out what the best fit is. We pride ourselves on highly personal service, and we travel the country to learn about schools. The visual we have used on our website is a picture of a graduation caps tossed into the blue sky. See my website.

Target Market(s)

Parents of high school students

Industry/Entity Type

Travel

Contact Information for Business Card

COLLEGE IS THE DREAM. LET US HELP YOU FIND THE DESTINATION.

Norah Velquist Dabney and Associates
College Admissions Advising and Essay Guidance
tovel@norahvelquistdabney-example.com
415-382-TEAM (8326)
Follow us on Friendloop

```html
<!DOCTYPE html>
<html lang="en">
<head>
<meta charset="utf-8">
<title>Norah Velquist – Business Card</title>
<link rel="stylesheet" href="https://fonts.googleapis.com/css2?family=Tinos&family=Open+Sans:wght@500&family=Arimo&display=swap">
<style>
  :root {
    --plum: #7a0868;
    --plum-dark: #4a0440;
    --ink: #111111;
    --paper: #ffffff;
    --frame: #9a9a9a;
    --backdrop: #ffffff;
  }
  * { margin: 0; padding: 0; box-sizing: border-box; }
  html, body {
    width: 1200px;
    height: 704px;
    overflow: hidden;
    background: var(--backdrop);
  }
  .card {
    position: absolute;
    left: 6px;
    top: 6px;
    width: 1180px;
    height: 686px;
    background: var(--paper);
    border: 1px solid var(--frame);
    box-shadow: 4px 5px 8px rgba(0,0,0,0.45);
    overflow: hidden;
  }
  .card__art {
    position: absolute;
    inset: 0;
    width: 100%;
    height: 100%;
  }
  .slogan {
    font-family: "Tinos", "Times New Roman", serif;
    fill: var(--paper);
    font-size: 50px;
    letter-spacing: 1px;
  }
  .advisor-name {
    position: absolute;
    left: 640px;
    top: 22px;
    font-family: "Tinos", "Times New Roman", serif;
    font-size: 66px;
    line-height: 1;
    color: var(--ink);
    white-space: nowrap;
  }
  .advisor-name__last { color: var(--plum); }
  .firm-name {
    position: absolute;
    left: 680px;
    top: 146px;
    font-family: "Open Sans", Arial, sans-serif;
    font-weight: 500;
    font-size: 28px;
    color: var(--ink);
    white-space: nowrap;
    transform: scaleX(0.92);
    transform-origin: left;
  }
  .contact {
    position: absolute;
    left: 14px;
    top: 465px;
    font-family: "Tinos", "Times New Roman", serif;
    font-size: 27px;
    line-height: 30px;
    color: var(--ink);
  }
  .contact__phone {
    font-family: "Arimo", Arial, sans-serif;
    font-size: 25px;
    padding-left: 4px;
  }
  .services {
    position: absolute;
    left: 0;
    right: 0;
    top: 654px;
    padding-left: 20px;
    text-align: center;
    font-family: "Arimo", Arial, sans-serif;
    font-size: 25px;
    color: var(--ink);
  }
</style>
</head>
<body>
  <div class="card">
    <svg class="card__art" viewBox="0 0 1088 638" preserveAspectRatio="none" aria-hidden="true">
      <defs>
        <filter id="band-shadow" x="-5%" y="-5%" width="115%" height="120%">
          <feDropShadow dx="3" dy="4" stdDeviation="3" flood-color="#000" flood-opacity="0.45"/>
        </filter>
        <filter id="emboss" x="-5%" y="-20%" width="110%" height="150%">
          <feDropShadow dx="2" dy="3" stdDeviation="1.5" flood-color="#2a0024" flood-opacity="0.9"/>
        </filter>
        <path id="slogan-upper" d="M342,36 C500,150 700,290 880,300 C960,305 1010,305 1068,300"/>
        <path id="slogan-lower" d="M10,205 C200,222 350,262 500,322 C700,405 880,495 1088,522"/>
      </defs>
      <path class="wave-band" fill="var(--plum)" filter="url(#band-shadow)"
            d="M0,0 L355,0 C520,110 720,250 900,255 C990,258 1040,248 1078,240 L1078,497 C900,512 700,440 500,360 C330,292 150,250 0,245 Z"/>
      <g filter="url(#emboss)">
        <text class="slogan"><textPath href="#slogan-upper" textLength="735" lengthAdjust="spacingAndGlyphs">COLLEGE IS THE DREAM.</textPath></text>
        <text class="slogan"><textPath href="#slogan-lower" textLength="1120" lengthAdjust="spacingAndGlyphs">LET US HELP YOU FIND THE DESTINATION.</textPath></text>
      </g>
    </svg>

    <h1 class="advisor-name">Norah <span class="advisor-name__last">Velquist</span></h1>
    <p class="firm-name">Dabney and Associates College</p>

    <address class="contact" style="font-style: normal;">
      <div class="contact__email">tovel@norahvelquistdabney-example.com</div>
      <div class="contact__social">Follow us on Friendloop</div>
      <div class="contact__phone">415-382-TEAM (8326)</div>
    </address>

    <p class="services">Admissions Advising and Essay Guidance</p>
  </div>
</body>
</html>
```